Verodex business card

Business card for sustainable investment company called "Verodex". Verodex is an exchange platform selling carbon credits between buyers and sellers. Carbon Credits are an environmental commodity for reducing global carbon emissions.

the card should obviously have our logo and the theme should be sustainability/environment mixed with a trading platform.

Contact Information for Business Card

Logo, Name, Title, Phone, Email

Colors
0054AA
0677BA
7BADD7
CADEEF
E8F1F8
0094D4
00A9DD
6FCCEA
C7EBF8
E9F6FB
00AB8E
00BBA5
67D7C9
C6EFE9
E9F9F6
59FF00
82FF00
B8FF75
E3FFCB
F4FFEA

```html
<!DOCTYPE html>
<html lang="en">
<head>
<meta charset="utf-8">
<title>Verodex business card</title>
<link href="https://fonts.googleapis.com/css2?family=Montserrat:wght@400;500;600;700&display=swap" rel="stylesheet">
<style>
  :root {
    --backdrop: #3a322d;
    --paper: #ffffff;
    --navy: #172a4f;
    --navy-deep: #121e3d;
    --sky: #2aa6e2;
    --sky-soft: #6fb4e6;
    --ink: #2b2f36;
    --pattern-light: #8fb2e3;
    --pattern-dark: #1a2749;
  }
  * { box-sizing: border-box; margin: 0; padding: 0; }
  html, body { width: 1200px; height: 786px; overflow: hidden; }
  body {
    background: var(--backdrop);
    font-family: "Montserrat", Arial, sans-serif;
    position: relative;
  }
  .card {
    position: absolute;
    top: 238px;
    width: 540px;
    height: 309px;
    border-radius: 4px;
    overflow: hidden;
    box-shadow: 0 14px 30px rgba(0,0,0,.35);
  }
  /* Front */
  .card-front { left: 40px; background: var(--paper); }
  .brand-name {
    position: absolute;
    left: 36px; top: 40px;
    font-weight: 700;
    font-size: 60px;
    letter-spacing: 1px;
    color: var(--navy);
  }
  .brand-dot {
    position: absolute;
    right: 46px; top: 96px;
    width: 120px; height: 120px;
    border-radius: 50%;
    background: var(--sky);
  }
  .person-name {
    position: absolute;
    left: 36px; top: 150px;
    font-weight: 700;
    font-size: 20px;
    color: var(--sky);
  }
  .person-title {
    position: absolute;
    left: 36px; top: 176px;
    font-size: 12px;
    font-weight: 500;
    color: var(--ink);
  }
  .address {
    position: absolute;
    left: 36px; top: 206px;
    font-size: 12px;
    line-height: 16px;
    color: var(--ink);
  }
  .contact-list {
    position: absolute;
    left: 36px; top: 248px;
    list-style: none;
    font-size: 12px;
    line-height: 17px;
    color: var(--ink);
  }
  .contact-list li { display: flex; align-items: center; gap: 8px; }
  .contact-list svg { width: 10px; height: 10px; fill: var(--sky); }
  /* Back */
  .card-back {
    left: 620px;
    background: var(--navy-deep);
  }
  .brand-pattern {
    position: absolute;
    inset: 0;
    background: linear-gradient(120deg, var(--pattern-light) 0%, #3d5a93 45%, var(--pattern-dark) 100%);
    opacity: .55;
  }
  .back-name {
    position: absolute;
    right: 42px; top: 132px;
    font-weight: 700;
    font-size: 18px;
    letter-spacing: 1px;
    color: var(--sky);
  }
</style>
</head>
<body>
  <section class="card card-front">
    <div class="brand-name">VERODEX</div>
    <div class="brand-dot"></div>
    <div class="person-name">Marco Ellison</div>
    <div class="person-title">CEO &amp; Founder</div>
    <div class="address">48 Harbor Lane, Suite 210<br>Eastfield, PA 17602</div>
    <ul class="contact-list">
      <li><svg viewBox="0 0 10 10"><path d="M2 0h2l1 3-1.5 1a6 6 0 0 0 2.5 2.5L7 5l3 1v2c0 1-1 2-2 2A8 8 0 0 1 0 2c0-1 1-2 2-2z"/></svg>(37) 555-0182</li>
      <li><svg viewBox="0 0 10 10"><path d="M0 2h10v6H0zM0 2l5 3.5L10 2" stroke="#fff" stroke-width=".8"/></svg>info@verodex.com</li>
      <li><svg viewBox="0 0 10 10"><circle cx="5" cy="5" r="5"/><path d="M0 5h10M5 0v10" stroke="#fff" stroke-width=".7"/></svg>www.verodex.com</li>
    </ul>
  </section>

  <section class="card card-back">
    <div class="brand-pattern" role="img" aria-label="Repeating pattern of the brand mark in glossy blue tones"></div>
    <div class="back-name">VERODEX</div>
  </section>
</body>
</html>
```